Business card design needed

Hello, I Need a business card for a company that specialises in providing contract management services for civil construction projects - roads, bridges etc.
I do have a logo that i produced for PLOVER Civilworks however it probably needs a little work, the circles dont have defined edges, i was thinking the colours should reflect the dry interior of Australia progressing out to the colours of the ocean as you move towards the East.... that was my thinking anyway!
Target Market(s)
Professional people generally 30+ yrs old who need professional services to deliver contracts in a high risk environment
Industry/Entity Type
Construction
Contact Information for Business Card
PLOVER Civilworks
Darren Pollock - Director and Principal Engineer
Registered Professional Engineer of Queensland
Phone 0491 265 807
Email darren@plovercivilworks.com.au
ABN 48 213 670 194
Logo Text
PLOVER Civilworks
Logo styles of interest
Pictorial/Combination Logo
Wordmark Logo
Lettermark Logo
Look and feel

```html
<!DOCTYPE html>
<html lang="en">
<head>
<meta charset="utf-8">
<title>PLOVER Civilworks – Business Card</title>
<link rel="stylesheet" href="https://fonts.googleapis.com/css2?family=Bebas+Neue&family=Open+Sans:wght@400;700&display=swap">
<style>
  :root {
    --bg: #1e1e1e;
    --card: #f1f1f1;
    --green: #55a98a;
    --red: #d9442e;
    --name: #5d7270;
    --ink: #2b2b2b;
    --muted: #555;
    --silver-a: #b4b9bd;
    --silver-b: #d6d9dc;
  }
  * { margin: 0; padding: 0; box-sizing: border-box; }
  html, body { width: 1200px; height: 1000px; overflow: hidden; }
  body {
    background: var(--bg);
    display: flex;
    flex-direction: column;
    align-items: center;
    justify-content: center;
    gap: 40px;
  }
  .card {
    position: relative;
    width: 700px;
    height: 400px;
    background: var(--card);
    overflow: hidden;
    box-shadow: 0 10px 30px rgba(0,0,0,.5);
  }

  /* Front */
  .edge-band { position: absolute; left: 0; width: 48px; }
  .edge-band--top { top: 0; height: 232px; background: var(--green); }
  .edge-band--mid { top: 244px; height: 40px; background: var(--red); }
  .edge-band--bottom { top: 296px; height: 104px; background: var(--green); }
  .corner-block {
    position: absolute; right: 0; top: 40px;
    width: 64px; height: 34px; background: var(--green);
  }
  .accent-bar {
    position: absolute; right: 0; top: 170px;
    width: 360px; height: 30px; background: var(--red);
  }
  .holder {
    position: absolute; right: 76px; top: 38px; text-align: right;
  }
  .holder__name {
    font-family: "Bebas Neue", sans-serif;
    font-size: 40px; letter-spacing: 1px; line-height: 1;
    color: var(--name);
  }
  .holder__role {
    font-family: "Open Sans", sans-serif;
    font-size: 11px; font-weight: 700; line-height: 1.4; color: var(--muted);
  }
  .holder__reg {
    font-family: "Open Sans", sans-serif;
    font-size: 10px; font-weight: 400; line-height: 1.4; color: var(--muted);
  }
  .company {
    position: absolute; left: 70px; top: 196px;
    font-family: "Bebas Neue", sans-serif;
    font-size: 34px; letter-spacing: 1px; line-height: 1; color: var(--ink);
  }
  .contact {
    position: absolute; left: 130px; top: 246px;
    list-style: none;
    font-family: "Open Sans", sans-serif;
    font-size: 14px; line-height: 1.45; color: var(--muted);
  }
  .contact b { color: var(--ink); }

  /* Back */
  .logo-panel {
    position: absolute; inset: 34px;
    background: linear-gradient(100deg, var(--silver-a) 0%, var(--silver-b) 35%, var(--silver-a) 60%, var(--silver-b) 85%, var(--silver-a) 100%);
    display: flex; align-items: center; justify-content: center;
  }
  .logo-panel__name {
    font-family: "Open Sans", sans-serif;
    font-weight: 400; font-size: 46px; color: var(--ink);
  }
</style>
</head>
<body>
  <section class="card card--front" aria-label="Business card front">
    <div class="edge-band edge-band--top"></div>
    <div class="edge-band edge-band--mid"></div>
    <div class="edge-band edge-band--bottom"></div>
    <div class="corner-block"></div>
    <div class="accent-bar"></div>
    <div class="holder">
      <h1 class="holder__name">Darren Pollock</h1>
      <p class="holder__role">Director and Principal Engineer</p>
      <p class="holder__reg">Registered Professional Engineer of Queensland</p>
    </div>
    <h2 class="company">PLOVER Civilworks</h2>
    <ul class="contact">
      <li><b>Phone</b> 0491 265 807</li>
      <li><b>Email</b> darren@plovercivilworks.com.au</li>
      <li><b>ABN</b> 48 213 670 194</li>
    </ul>
  </section>

  <section class="card card--back" aria-label="Business card back">
    <div class="logo-panel">
      <span class="logo-panel__name">PLOVER Civilworks</span>
    </div>
  </section>
</body>
</html>
```